QuillVex is a crypto-arbitrage tool that finds arbitrages between and within exchanges.A logo for the websiteA designer will need to design main page which will describe the project.A subscription page which will have subscription packages. A client portal page where client can set filter types, payment options etc...A Solutions page which will have the actual solutions which quillVex will calculate. Other pages that have to do with login and subscribing. We need all this to be done as a project with actual color numbers high quality images. ETC... We have attached the current Mock up but designer should have their own input and make it better.
Updates
Project is large and people need time to get it done, please extend by 3 weeks
Need more time to get the project finished right
Target Market(s)
Crypto Traders that are looking to make more money trading
Industry/Entity Type
Finance
Coding
Coded - Design and coding required
Number of Pages Required
5+ page
Colors
Designer to choose colors to be used in the design.
Requirements
Nice to have
- Good animations

```html
<!DOCTYPE html>
<html lang="en">
<head>
<meta charset="utf-8">
<title>QuillVex — Login</title>
<link rel="stylesheet" href="https://fonts.googleapis.com/css2?family=Lato:wght@700;900&family=Roboto:wght@400;500&display=swap">
<style>
  :root {
    --teal: #2497ad;
    --teal-deep: #1d8599;
    --teal-light: #3aa8bc;
    --paper: #f6f6f6;
    --paper-shade: #ececec;
    --white: #ffffff;
    --ink: #1f1f1f;
    --text: #555555;
    --field-border: #b9b9b9;
  }
  * { box-sizing: border-box; margin: 0; padding: 0; }
  html, body { width: 1200px; height: 734px; overflow: hidden; }
  body { position: relative; font-family: "Roboto", Arial, sans-serif; background: var(--paper); }

  .hero-visual {
    position: absolute; left: 0; top: 0; width: 601px; height: 734px;
    background: radial-gradient(ellipse at 35% 70%, var(--teal-light) 0%, var(--teal) 45%, var(--teal-deep) 100%);
  }
  .network-visual {
    position: absolute; left: 601px; top: 0; width: 599px; height: 734px;
    background: linear-gradient(180deg, var(--paper) 0%, var(--paper) 45%, var(--paper-shade) 100%);
  }

  .brand {
    position: absolute; left: 111px; top: 26px;
    font-family: "Lato", Arial, sans-serif; font-weight: 900; font-size: 31px;
    color: var(--white); letter-spacing: 0.3px;
  }
  .menu-toggle { position: absolute; left: 1059px; top: 32px; width: 30px; height: 24px; }
  .menu-toggle span {
    display: block; height: 4px; background: var(--teal); border-radius: 1px; margin-bottom: 6px;
  }

  .login-card {
    position: absolute; left: 356px; top: 100px; width: 489px; height: 504px;
    background: var(--white); box-shadow: 0 2px 10px rgba(0,0,0,0.12);
  }
  .login-title {
    position: absolute; left: 0; right: 0; top: 148px; text-align: center;
    font-family: "Lato", Arial, sans-serif; font-weight: 900; font-size: 31px; color: var(--ink);
    line-height: 40px;
  }
  .field {
    position: absolute; left: 411px; width: 378px; height: 45px;
    border: 1px solid var(--field-border); background: var(--white);
    font-size: 14.5px; color: var(--text); padding-left: 17px; line-height: 43px;
  }
  .field.username { top: 222px; }
  .field.password { top: 277px; }

  .option {
    position: absolute; left: 411px; font-size: 14.5px; color: var(--text);
    display: flex; align-items: center; line-height: 18px;
  }
  .option svg { margin-right: 7px; }
  .option.show-password { top: 354px; }
  .option.keep-signed { top: 386px; }

  .sign-in {
    position: absolute; left: 411px; top: 447px; width: 378px; height: 45px;
    background: var(--teal); color: var(--white);
    font-weight: 500; font-size: 19px; text-align: center; line-height: 45px;
  }

  .new-account {
    position: absolute; left: 410px; top: 529px; font-size: 15.5px; color: var(--text);
  }
  .create-account {
    position: absolute; right: 411px; top: 529px; font-size: 15.5px; color: var(--teal);
    display: flex; align-items: center; border-bottom: 1px solid var(--teal); line-height: 18px;
  }
  .create-account svg { margin-left: 8px; }

  .copyright {
    position: absolute; left: 111px; top: 684px; font-size: 14.5px; color: var(--white);
  }
  .social { position: absolute; top: 683px; width: 33px; height: 33px; border: 1.5px solid var(--white); border-radius: 50%; }
  .social.one { left: 1010px; }
  .social.two { left: 1053px; }
</style>
</head>
<body>
  <div class="hero-visual" role="img" aria-label="Teal-tinted photo of crypto coins beneath a network mesh"></div>
  <div class="network-visual" role="img" aria-label="Faint grey world map and connected network pattern"></div>

  <div class="brand">QUILLVEX</div>
  <div class="menu-toggle"><span></span><span></span><span></span></div>

  <div class="login-card"></div>
  <h1 class="login-title">LOGIN</h1>

  <div class="field username">User Name</div>
  <div class="field password">Password</div>

  <div class="option show-password">
    <svg width="13" height="13" viewBox="0 0 13 13"><circle cx="6.5" cy="6.5" r="5.5" fill="none" stroke="#555" stroke-width="1.6"/><circle cx="6.5" cy="6.5" r="2.3" fill="#555"/></svg>
    Show Password
  </div>
  <div class="option keep-signed">
    <svg width="13" height="13" viewBox="0 0 13 13"><circle cx="6.5" cy="6.5" r="5.5" fill="none" stroke="#555" stroke-width="1.6"/></svg>
    Keep Me Signed
  </div>

  <div class="sign-in">SIGN IN</div>

  <div class="new-account">New Account</div>
  <div class="create-account">Create New Account
    <svg width="14" height="14" viewBox="0 0 14 14"><circle cx="7" cy="7" r="7" fill="#2497ad"/><path d="M3.5 7h6M7 4.2 9.8 7 7 9.8" fill="none" stroke="#fff" stroke-width="1.8" stroke-linecap="round" stroke-linejoin="round"/></svg>
  </div>

  <div class="copyright">© Copyright 2019 QuillVex. All Rights Reserved</div>
  <div class="social one"></div>
  <div class="social two"></div>
</body>
</html>
```